Book Cover Design for The Banker's Riddle

We need a bold, attention-getting design for a book on a revolutionary new way of funding government spending - not only could we eliminate income taxes and finally balance the budget, but we could afford to pay everyone a basic income, provide free healthcare, free college, and a guaranteed retirement. See www.TheBankersRiddle.net to understand the proposition.

The book title is: The Banker's Riddle

The subtitle is: If Our Country Were Managed Wisely, We Would Skip Taxes, We'd Collect Returns

The author's name is: Derek Hale

Target Market(s)

General population

Industry/Entity Type

Government

Font styles to use
Sans Serif

Requirements
Must have
• The blurb about the book, and about the author should be on the back cover, as should the author's photo.
• The book will be 5.5 x 8.5 inches and 165 pages long
Nice to have
• The subtitle should be prominent on the front cover, perhaps even above the title. The designer can use the sunrise photo as we do on the website to feature the subtitle, or not. We are open to all designs.

```html
<!DOCTYPE html>
<html lang="en">
<head>
<meta charset="utf-8">
<title>The Banker's Riddle – Cover Layout</title>
<link href="https://fonts.googleapis.com/css2?family=Arimo:wght@400;500&display=swap" rel="stylesheet">
<style>
  :root {
    --page: #ffffff;
    --ink: #111111;
    --white: #ffffff;
    --sun-core: #f1e4e0;
    --sun-glow: #f6b04a;
    --orange: #e0761e;
    --burnt: #b8461a;
    --rust: #8f2f16;
    --deep: #4a1a10;
    --flap-top: #d8a88a;
    --flap-mid: #c88a70;
    --flap-low: #b37768;
    --spine: #d69a7c;
  }
  * { box-sizing: border-box; margin: 0; padding: 0; }
  html, body { width: 1200px; height: 701px; overflow: hidden; background: var(--page); }
  body { font-family: "Arimo", Arial, sans-serif; color: var(--white); position: relative; }

  .dimension { position: absolute; color: var(--ink); font-size: 19px; }
  .dimension-line { position: absolute; height: 1px; background: var(--ink); }
  .dimension-line.vertical { width: 1px; height: auto; }

  .panel { position: absolute; top: 54px; height: 645px; overflow: hidden; }
  .flap-left { left: 0; width: 119px;
    background: linear-gradient(180deg, var(--flap-top) 0%, var(--flap-mid) 45%, var(--flap-low) 100%); }
  .flap-right { left: 1029px; width: 111px;
    background: linear-gradient(180deg, var(--flap-top) 0%, var(--flap-mid) 45%, #a87672 100%); }
  .back-cover { left: 119px; width: 418px;
    background: linear-gradient(180deg, var(--orange) 0%, #d36420 30%, var(--burnt) 60%, var(--rust) 100%); }
  .spine { left: 537px; width: 73px;
    background: linear-gradient(180deg, var(--spine) 0%, #cf8a68 40%, #c37b63 100%); }
  .front-cover { left: 610px; width: 419px;
    background:
      radial-gradient(circle at 158px 186px, var(--sun-core) 0, #f5d6c0 35px, var(--sun-glow) 90px, var(--orange) 180px, var(--burnt) 330px, var(--rust) 470px, var(--deep) 620px); }

  .blurb { position: absolute; left: 31px; width: 366px; font-size: 13px; line-height: 14.1px; }
  .blurb p + p { margin-top: 13px; }
  .blurb-book { top: 47px; }
  .blurb-author { top: 492px; }

  .author-photo { position: absolute; left: 31px; top: 304px; width: 109px; height: 144px;
    background: linear-gradient(180deg, #8a7f4a 0%, #5b5a34 55%, #2c2a22 100%); }
  .author-caption { position: absolute; left: 31px; top: 449px; width: 109px; text-align: center; font-size: 14px; }

  .spine-text { position: absolute; left: 50%; white-space: nowrap; transform-origin: center; }
  .spine-author { top: 136px; font-size: 18px; transform: translate(-50%, -50%) rotate(-90deg); }
  .spine-title { top: 426px; font-size: 29px; transform: translate(-50%, -50%) rotate(-90deg); }

  .title { position: absolute; top: 80px; left: 0; width: 100%; text-align: center; font-weight: 400; }
  .title-article { display: block; font-size: 21px; line-height: 22px; }
  .title-main { display: block; font-size: 46px; line-height: 46px; }
  .subtitle { position: absolute; top: 434px; left: 0; width: 100%; text-align: center;
    font-size: 25px; line-height: 30.5px; }
</style>
</head>
<body>
  <span class="dimension" style="left:42px;top:3px;">1.47”</span>
  <div class="dimension-line" style="left:0;top:42px;width:114px;"></div>
  <span class="dimension" style="left:297px;top:-4px;">5.5”</span>
  <div class="dimension-line" style="left:119px;top:30px;width:418px;"></div>
  <span class="dimension" style="left:548px;top:12px;">.97”</span>
  <div class="dimension-line" style="left:537px;top:42px;width:73px;"></div>
  <span class="dimension" style="left:790px;top:-4px;">5.5”</span>
  <div class="dimension-line" style="left:613px;top:30px;width:416px;"></div>
  <span class="dimension" style="left:1070px;top:3px;">1.47”</span>
  <div class="dimension-line" style="left:1029px;top:42px;width:111px;"></div>
  <div class="dimension-line vertical" style="left:1150px;top:54px;height:645px;"></div>
  <span class="dimension" style="left:1163px;top:340px;">8.5”</span>

  <div class="panel flap-left" role="img" aria-label="Faded photo of misty mountains and pine forest at sunrise"></div>

  <section class="panel back-cover">
    <div class="back-photo" role="img" aria-label="Sunrise photo of mountains and pine forest in orange tones" style="position:absolute;inset:0;"></div>
    <div class="blurb blurb-book">
      <p>This is the story of how technology can transform our economy. If we play it right, we can all win. When combined with a new understanding of money, technology can eliminate the need for income taxes while balancing the budget and paying off the national debt. We can even afford a National Income, free higher education, and free healthcare, while vastly reducing poverty.</p>
      <p>The solutions herein are nonpartisan, benefiting both rich and poor. They could enable our nation to reach greater heights of prosperity than we have ever achieved before. The answer is in restructuring our financial system to stoke the production engine that technology enables, instead of taxing prosperity as we do today.</p>
    </div>
    <div class="author-photo" role="img" aria-label="Portrait photo of the author"></div>
    <div class="author-caption">Derek Hale</div>
    <div class="blurb blurb-author">
      <p>Hale pioneered structured finance on Wall Street, architected the financing for Thabo Mensah’s Redevelopment Program, co-founded two nationally acclaimed charter schools, co-founded several successful technology companies and launched a publication for students read by millions in dozens of countries. He has six children, lives with his wife in Aspen Ridge, Montana and Georgia, and enjoys solving national economic problems</p>
    </div>
  </section>

  <section class="panel spine">
    <span class="spine-text spine-author">By : Derek Hale</span>
    <span class="spine-text spine-title">The Banker's Riddle</span>
  </section>

  <section class="panel front-cover">
    <div role="img" aria-label="Sunrise over mountains and pine forest" style="position:absolute;inset:0;"></div>
    <h1 class="title">
      <span class="title-article">The</span>
      <span class="title-main">Banker's Riddle</span>
    </h1>
    <p class="subtitle">If Our Country Were Managed Wisely,<br>We Would Skip Taxes, We'd<br>Collect Returns</p>
  </section>

  <div class="panel flap-right" role="img" aria-label="Faded photo of pine forest in morning mist"></div>
</body>
</html>
```